Sandwich board

We are a Photo booth company in NZ.
We need a sandwich board design we have all the guts and we know the style we want just need help making it look good/right.
Dimension of the board are 59cm by 69cm.
The other side is a chalk board so we can write about the event we are at.
The board is a light white wash ply and we will be applying by stencil or dye cut vinyl.
The words are
Just grab a prop
and strike a pose
take your own
black and white or colour
photos
And a carriage with a camera in the back.

Reason: I would like to see a bit more of a play around with the fonts and style.

Target Market(s)

this will be at event mostly weddings, birthdays, fairs really any event.

Industry/Entity Type

Camera

Requirements
Must have
• it must be black with white back ground
Nice to have
• simple lines
Should not have
• colour. to much little detail.

```html
<!DOCTYPE html>
<html lang="en">
<head>
<meta charset="utf-8">
<title>Just Grab a Prop – Sandwich Board</title>
<link href="https://fonts.googleapis.com/css2?family=Rye&family=Sancreek&family=Playfair+Display:wght@400&family=Archivo+Black&display=swap" rel="stylesheet">
<style>
  :root {
    --board: #ffffff;
    --ink: #111111;
    --ink-art: #2a2a2a;
    --ink-orn: #cfcfcf;
  }
  html, body {
    margin: 0;
    padding: 0;
    width: 900px;
    height: 1200px;
    overflow: hidden;
    background: var(--board);
  }
  .board {
    display: block;
    width: 900px;
    height: 1200px;
  }
  .rule { stroke: var(--ink); fill: none; }
  .ink { fill: var(--ink); }
  .art { fill: var(--ink-art); }
  .ornament { fill: var(--ink-orn); }
  .headline-just { font-family: "Rye", serif; font-size: 100px; }
  .headline-prop { font-family: "Sancreek", serif; font-size: 92px; }
  .headline-strike { font-family: "Playfair Display", serif; font-size: 136px; }
  .headline-pose { font-family: "Sancreek", serif; font-size: 90px; }
  .line-take { font-family: "Archivo Black", sans-serif; font-size: 44px; }
  .line-colours { font-family: "Playfair Display", serif; font-size: 48px; }
  .headline-photos { font-family: "Sancreek", serif; font-size: 128px; }
  .ribbon-word { font-family: "Archivo Black", sans-serif; font-size: 13px; fill: var(--board); }
  .ribbon-word-small { font-family: "Archivo Black", sans-serif; font-size: 10px; fill: var(--board); }
  .monogram { font-family: "Playfair Display", serif; font-size: 40px; }
</style>
</head>
<body>
<svg class="board" viewBox="0 0 900 1200" xmlns="http://www.w3.org/2000/svg">
  <!-- corner flourishes -->
  <rect class="ornament" x="28" y="86" width="92" height="92" role="img" aria-label="Corner scroll flourish"/>
  <rect class="ornament" x="780" y="86" width="92" height="92" role="img" aria-label="Corner scroll flourish"/>
  <rect class="ornament" x="28" y="1022" width="92" height="92" role="img" aria-label="Corner scroll flourish"/>
  <rect class="ornament" x="780" y="1022" width="92" height="92" role="img" aria-label="Corner scroll flourish"/>

  <!-- outer board edges -->
  <line class="rule" x1="0" y1="74" x2="900" y2="74" stroke-width="3"/>
  <line class="rule" x1="0" y1="1127" x2="900" y2="1127" stroke-width="3"/>
  <!-- inner frame -->
  <rect class="rule" x="112" y="95" width="676" height="1015" rx="14" stroke-width="2"/>

  <!-- top divider -->
  <g class="divider-top">
    <line class="rule" x1="210" y1="127" x2="690" y2="127" stroke-width="3"/>
    <circle class="rule" cx="450" cy="127" r="15" stroke-width="4"/>
    <circle class="ink" cx="450" cy="127" r="6"/>
  </g>

  <text class="headline-just ink" x="450" y="243" text-anchor="middle" textLength="310" lengthAdjust="spacingAndGlyphs">JUST</text>
  <text class="headline-prop ink" x="457" y="338" text-anchor="middle" textLength="585" lengthAdjust="spacingAndGlyphs">GRAB A PROP</text>

  <!-- "and" divider -->
  <g class="divider-and">
    <line class="rule" x1="245" y1="390" x2="385" y2="390" stroke-width="3"/>
    <line class="rule" x1="520" y1="390" x2="655" y2="390" stroke-width="3"/>
    <circle class="ink" cx="262" cy="390" r="5"/>
    <circle class="ink" cx="638" cy="390" r="5"/>
    <polygon class="ink" points="398,376 505,370 498,404 392,410"/>
    <text class="ribbon-word" x="449" y="395" text-anchor="middle">AND</text>
  </g>

  <text class="headline-strike ink" x="449" y="528" text-anchor="middle" textLength="455" lengthAdjust="spacingAndGlyphs">STRIKE</text>

  <!-- "a" monogram with foliage -->
  <g class="divider-monogram">
    <rect class="art" x="285" y="578" width="120" height="40" rx="20" role="img" aria-label="Leafy scroll flourish"/>
    <rect class="art" x="495" y="578" width="120" height="40" rx="20" role="img" aria-label="Leafy scroll flourish"/>
    <circle cx="450" cy="600" r="34" fill="var(--board)" class="rule" stroke-width="3"/>
    <circle class="rule" cx="450" cy="600" r="27" stroke-width="1.5"/>
    <text class="monogram ink" x="450" y="614" text-anchor="middle">A</text>
  </g>

  <text class="headline-pose ink" x="452" y="712" text-anchor="middle" textLength="195" lengthAdjust="spacingAndGlyphs">POSE</text>

  <!-- small divider -->
  <g class="divider-small">
    <line class="rule" x1="345" y1="740" x2="555" y2="740" stroke-width="2"/>
    <circle class="rule" cx="450" cy="740" r="7" stroke-width="2.5"/>
    <circle class="ink" cx="450" cy="740" r="3"/>
  </g>

  <text class="line-take ink" x="450" y="803" text-anchor="middle" textLength="420" lengthAdjust="spacingAndGlyphs">TAKE YOUR OWN</text>

  <g class="line-colours ink">
    <text x="128" y="867" textLength="158" lengthAdjust="spacingAndGlyphs">BLACK</text>
    <polygon points="294,848 346,842 341,866 289,872"/>
    <text class="ribbon-word-small" x="318" y="861" text-anchor="middle">AND</text>
    <text x="356" y="867" textLength="170" lengthAdjust="spacingAndGlyphs">WHITE</text>
    <polygon points="538,848 590,842 585,866 533,872"/>
    <text class="ribbon-word-small" x="562" y="861" text-anchor="middle">OR</text>
    <text x="600" y="867" textLength="170" lengthAdjust="spacingAndGlyphs">COLOR</text>
  </g>

  <text class="headline-photos ink" x="450" y="988" text-anchor="middle" textLength="418" lengthAdjust="spacingAndGlyphs">PHOTOS</text>

  <!-- carriage scene -->
  <rect class="art" x="128" y="892" width="104" height="198" rx="6" role="img" aria-label="Vintage twin-lens camera riding on a carriage"/>
  <rect class="art" x="240" y="1005" width="130" height="86" rx="6" role="img" aria-label="Horse pulling the camera carriage"/>
  <rect class="art" x="380" y="1055" width="140" height="24" rx="12" role="img" aria-label="Scroll flourish"/>
  <rect class="art" x="530" y="1005" width="130" height="86" rx="6" role="img" aria-label="Horse pulling the camera carriage"/>
  <rect class="art" x="668" y="892" width="104" height="198" rx="6" role="img" aria-label="Vintage twin-lens camera riding on a carriage"/>
</svg>
</body>
</html>
```